Ardoise Lumen Stationery design

With my provided logo I need stationery design for business cards, envelope (#10), letterhead, fax sheet, memo sheet and 9'' x 12'' presentation folder. I would aIso need an email signature design included. PMS COLORS are : Pantone 541C et 299C. Looking for a bold look, minimalist yet eye-catching look.

```html
<!DOCTYPE html>
<html lang="en">
<head>
<meta charset="utf-8">
<title>Ardoise Lumen Stationery</title>
<link href="https://fonts.googleapis.com/css2?family=Montserrat:wght@500;600;700&family=Source+Sans+3:wght@400;600&family=Tinos:wght@400;700&display=swap" rel="stylesheet">
<style>
:root{
  --navy:#0f3d73;
  --sky:#0a9fdd;
  --board:#c4c4c4;
  --paper:#ffffff;
  --ink:#2b2b2b;
  --label:#3a3a3a;
  --rule:#9aa4b0;
}
*{box-sizing:border-box;margin:0;padding:0}
html,body{width:811px;height:1200px;overflow:hidden;background:var(--board)}
body{position:relative;font-family:"Source Sans 3",sans-serif;color:var(--ink)}
.piece{position:absolute;background:var(--paper);box-shadow:0 1px 3px rgba(0,0,0,.25)}
.label{position:absolute;font-family:"Source Sans 3",sans-serif;font-weight:600;font-size:12px;color:var(--label);letter-spacing:.2px;text-align:center}
.brand{display:flex;align-items:center;gap:6px;font-family:"Montserrat",sans-serif;font-weight:700;color:var(--navy);letter-spacing:.04em;white-space:nowrap}
.brand.stack{flex-direction:column;gap:4px}
.brand .mark{border:2px solid currentColor;flex:none}
.brand.light{color:#fff}
.top-band{position:absolute;left:0;right:0;top:0;height:5px;background:var(--sky)}
.contact-list{position:absolute;font-size:6.2px;line-height:10.5px;color:var(--ink)}
.contact-list li{list-style:none;display:flex;align-items:center;gap:4px}
.contact-list svg{width:6px;height:6px;fill:var(--sky)}
.web-pill{position:absolute;left:0;background:var(--navy);color:#fff;font-size:7px;display:flex;align-items:center;gap:4px;padding:0 10px 0 22px;border-radius:0 10px 10px 0}
.web-pill svg{width:7px;height:7px;fill:none;stroke:#fff;stroke-width:1.4}

/* hero brand */
.hero{position:absolute;left:77px;top:52px}
.hero .brand{font-size:34px;gap:14px}
.hero .mark{width:48px;height:48px;border-width:4px}

/* email signature */
.sig{left:61px;top:147px;width:284px;height:65px}
.sig .brand{position:absolute;left:0;width:123px;top:10px;font-size:9px}
.sig .mark{width:18px;height:18px}
.sig-panel{position:absolute;left:123px;top:0;right:0;bottom:4px;background:var(--navy)}
.sig-band{position:absolute;left:0;right:0;bottom:0;height:4px;background:var(--sky)}
.sig-photo{position:absolute;left:18px;top:9px;width:38px;height:44px;background:linear-gradient(#e2e2e2,#8c8c8c)}
.sig-text{position:absolute;left:66px;top:7px;color:#fff;font-family:"Montserrat",sans-serif}
.sig-text .name{font-size:11px;font-weight:700}
.sig-text .role{font-size:6px;font-style:italic;margin-bottom:6px}
.sig-text .line{font-size:6.5px;line-height:10px}

/* fax */
.fax{left:61px;top:245px;width:283px;height:365px}
.fax .brand{position:absolute;left:0;right:0;top:22px;font-size:13px}
.fax .mark{width:22px;height:22px}
.fax-form{position:absolute;left:49px;top:92px;width:183px;font-family:"Tinos",serif;font-weight:700;font-size:5.5px}
.fax-row{display:flex;gap:8px;margin-bottom:8px}
.fax-field{flex:1;display:flex;align-items:flex-end}
.fax-field span{white-space:nowrap}
.fax-field i{flex:1;border-bottom:.6px solid #333;margin-left:1px;height:5px}
.fax-gap{height:20px}

/* business cards */
.card{top:645px;width:165px;height:99px}
.card-front{left:36px;background:var(--navy)}
.card-front .brand{position:absolute;left:0;width:92px;top:33px;font-size:7px}
.card-front .mark{width:14px;height:14px}
.card-info{position:absolute;left:92px;top:0;right:0;bottom:0;background:var(--paper);padding:14px 0 0 7px}
.card-info .name{font-family:"Montserrat",sans-serif;font-weight:700;font-size:7.5px;color:var(--sky)}
.card-info .role{font-size:4px;font-style:italic;margin-bottom:6px}
.card-info ul{list-style:none;font-size:3.4px}
.card-info li{display:flex;align-items:center;gap:4px;height:13px}
.card-info li b{width:7px;height:7px;border-radius:50%;border:1px solid var(--navy);margin-left:-4px;background:#fff}
.card-back{left:210px;background:var(--navy);display:flex;align-items:center;justify-content:center}
.card-back .brand{font-size:14px}
.card-back .mark{width:20px;height:20px}

/* letterhead */
.lh-under{position:absolute;left:55px;top:800px;width:281px;height:365px;background:var(--navy)}
.letter{left:36px;top:776px;width:282px;height:366px}
.letter .brand{position:absolute;left:21px;top:22px;font-size:12px}
.letter .mark{width:22px;height:22px}
.letter .contact-list{left:198px;top:33px}
.letter-body{position:absolute;left:22px;top:114px;width:240px;font-size:5px;line-height:8.2px;color:#222}
.letter-body .date{position:absolute;right:0;top:-6px}
.letter-body p{text-indent:13px;text-align:justify;margin-bottom:6px}
.letter-body .meta{margin-bottom:8px}
.sign-area{width:38px;height:10px;background:linear-gradient(90deg,#d0d0d0,#9a9a9a);margin:6px 0 3px}
.letter .web-pill{bottom:11px;height:14px}

/* memo */
.memo{left:469px;top:35px;width:282px;height:365px}
.memo .brand{position:absolute;left:21px;top:22px;font-size:12px}
.memo .mark{width:22px;height:22px}
.memo .contact-list{left:198px;top:33px}
.memo-lines{position:absolute;left:21px;right:21px;top:119px}
.memo-lines i{display:block;height:20px;border-bottom:.7px dashed var(--rule)}
.memo .web-pill{bottom:10px;height:15px}

/* envelope */
.env-front{left:441px;top:433px;width:337px;height:152px;overflow:hidden}
.env-front .brand{position:absolute;left:22px;top:20px;font-size:12px}
.env-front .mark{width:22px;height:22px}
.env-window{position:absolute;left:173px;top:22px;width:142px;height:49px;border:1px solid #bcbcbc;border-radius:5px;background:#fff}
.env-block{position:absolute;right:0;top:110px;width:70px;height:42px;background:var(--navy)}
.env-contact{position:absolute;left:22px;bottom:13px;font-size:7.5px;display:flex;gap:6px}
.env-back{left:443px;top:616px;width:338px;height:152px}
.env-flap{position:absolute;left:0;right:0;top:0}
.env-back .brand{position:absolute;left:0;right:0;top:90px;justify-content:center;font-size:15px}
.env-back .mark{width:20px;height:20px}

/* folder */
.folder{left:412px;top:814px;width:365px;height:376px;display:flex;background:none}
.folder-back{width:183px;background:var(--navy);position:relative}
.folder-back .brand{position:absolute;left:0;right:0;top:262px;font-size:12px}
.folder-back .mark{width:20px;height:20px}
.folder-back .contact-row{position:absolute;left:8px;right:8px;top:312px;display:flex;justify-content:space-between;color:#fff;font-size:4.5px}
.folder-front{flex:1;background:linear-gradient(160deg,#fff,#e9e9e9);position:relative}
.folder-front .brand{position:absolute;left:0;right:0;top:60px;font-size:16px}
.folder-front .mark{width:40px;height:40px}
.folder-title{position:absolute;left:0;right:0;top:210px;text-align:center;font-family:"Montserrat",sans-serif;font-weight:700;font-size:24px;color:var(--sky)}
.folder-front .web-pill{left:auto;right:0;bottom:40px;height:18px;border-radius:10px 0 0 10px;padding:0 12px;font-size:8px}
</style>
</head>
<body>

<div class="hero"><div class="brand"><span class="mark"></span>ARDOISE LUMEN</div></div>

<!-- email signature -->
<section class="piece sig">
  <div class="brand stack"><span class="mark"></span>ARDOISE LUMEN</div>
  <div class="sig-panel">
    <div class="sig-photo" role="img" aria-label="Portrait photo placeholder"></div>
    <div class="sig-text">
      <div class="name">NAME HERE</div>
      <div class="role">(Designation)</div>
      <div class="line">+1 555 010 2040</div>
      <div class="line">info@ardoiselumen.com</div>
    </div>
  </div>
  <div class="sig-band"></div>
</section>
<div class="label" style="left:61px;top:220px;width:284px">EMAIL SIGNATURE</div>

<!-- fax -->
<section class="piece fax">
  <div class="top-band"></div>
  <div class="brand stack"><span class="mark"></span>ARDOISE LUMEN</div>
  <div class="fax-form">
    <div class="fax-row"><div class="fax-field"><span>To:</span><i></i></div></div>
    <div class="fax-row"><div class="fax-field"><span>From:</span><i></i></div></div>
    <div class="fax-row"><div class="fax-field"><span>Re:</span><i></i></div></div>
    <div class="fax-gap"></div>
    <div class="fax-row"><div class="fax-field"><span>Fax #:</span><i></i></div><div class="fax-field"><span>Pages:</span><i></i></div></div>
    <div class="fax-row"><div class="fax-field"><span>Phone contact:</span><i></i></div><div class="fax-field"><span>Date:</span><i></i></div></div>
  </div>
</section>
<div class="label" style="left:61px;top:617px;width:283px">FAX SHEET</div>

<!-- business cards -->
<section class="piece card card-front">
  <div class="brand light stack"><span class="mark"></span>ARDOISE LUMEN</div>
  <div class="card-info">
    <div class="name">NAME HERE</div>
    <div class="role">Designation</div>
    <ul>
      <li><b></b>Address Goes Here</li>
      <li><b></b>Phone No. Goes Here</li>
      <li><b></b>Mail Goes Here</li>
      <li><b></b>Website Goes Here</li>
    </ul>
  </div>
</section>
<section class="piece card card-back">
  <div class="brand light"><span class="mark"></span>ARDOISE LUMEN</div>
</section>
<div class="label" style="left:36px;top:748px;width:165px">BUSINESS CARD ( FRONT )</div>
<div class="label" style="left:210px;top:748px;width:165px">BUSINESS CARD ( BACK)</div>

<!-- letterhead -->
<div class="lh-under"></div>
<section class="piece letter">
  <div class="top-band"></div>
  <div class="brand stack"><span class="mark"></span>ARDOISE LUMEN</div>
  <ul class="contact-list">
    <li><svg viewBox="0 0 10 10"><path d="M5 0a3.5 3.5 0 0 0-3.5 3.5C1.5 6 5 10 5 10s3.5-4 3.5-6.5A3.5 3.5 0 0 0 5 0z"/></svg>Address Goes Here</li>
    <li><svg viewBox="0 0 10 10"><path d="M2 0l2 2.5-1 1.5a6 6 0 0 0 3 3l1.5-1L10 8l-1.5 2C4 10 0 6 0 1.5z"/></svg>Phone no Goes Here</li>
    <li><svg viewBox="0 0 10 10"><path d="M0 2h10v6H0z M0 2l5 3.5L10 2" /></svg>Mail Goes Here</li>
  </ul>
  <div class="letter-body">
    <div class="date">Date: 19 Feb, 2020</div>
    <div class="meta">Your Name Here<br>Address</div>
    <p>Lorem ipsum dolor sit amet, consectetur adilpiscing elit. Suspendisse condimenttum egestas tellus et viverra. Vestibulum euismod lacus eget nisi ornare, id laoreet tortor dapibus. Dones lacinia euismod diam, convallis termpus risus, Ut et felis termpor eros blandit feugiat ut non enim, In vestibulum ligula blandit magna blandit dictum. Sed maiesuada erat id mauris pretium, ehet congue felis interdum. A enean ultricies enim nec lorem vestibulim, nec commodo quam sagittis, Cras bibendum mauris, eget aliquit semper, libero ipaum ultricies nunc, euismod pelenteque orci risus amet nibh, Maecenas feuiat mi a metus conwallis pharetra.</p>
    <p>Duis porta turpis ut pulvinar hendrerit elit lorem behichila turpls, lacinia semper pures ros ac nisi, Sed consectetur ante scienrisque tortor pellentesque imperdiet. Pellentesque habitant morbi tristique senectus et netus et malesuacia fames ac turpis egetas.</p>
    <div>Regards</div>
    <div class="sign-area" role="img" aria-label="Handwritten signature"></div>
    <div>Your Name Here<br>Designation Here</div>
  </div>
  <div class="web-pill"><svg viewBox="0 0 10 10"><circle cx="5" cy="5" r="4"/><path d="M1 5h8M5 1v8"/></svg>www.ardoiselumen.com</div>
</section>
<div class="label" style="left:36px;top:1170px;width:300px">LETTERHEAD DESIGN</div>

<!-- memo -->
<div class="label" style="left:469px;top:15px;width:282px">MEMO SHEET</div>
<section class="piece memo">
  <div class="top-band"></div>
  <div class="brand stack"><span class="mark"></span>ARDOISE LUMEN</div>
  <ul class="contact-list">
    <li><svg viewBox="0 0 10 10"><path d="M5 0a3.5 3.5 0 0 0-3.5 3.5C1.5 6 5 10 5 10s3.5-4 3.5-6.5A3.5 3.5 0 0 0 5 0z"/></svg>Address Goes Here</li>
    <li><svg viewBox="0 0 10 10"><path d="M2 0l2 2.5-1 1.5a6 6 0 0 0 3 3l1.5-1L10 8l-1.5 2C4 10 0 6 0 1.5z"/></svg>Phone no Goes Here</li>
    <li><svg viewBox="0 0 10 10"><path d="M0 2h10v6H0z M0 2l5 3.5L10 2"/></svg>Mail Goes Here</li>
  </ul>
  <div class="memo-lines"><i></i><i></i><i></i><i></i><i></i><i></i><i></i><i></i></div>
  <div class="web-pill"><svg viewBox="0 0 10 10"><circle cx="5" cy="5" r="4"/><path d="M1 5h8M5 1v8"/></svg>www.ardoiselumen.com</div>
</section>

<!-- envelope -->
<div class="label" style="left:441px;top:413px;width:337px">ENVELOPE ( FRONT )</div>
<section class="piece env-front">
  <div class="brand stack"><span class="mark"></span>ARDOISE LUMEN</div>
  <div class="env-window"></div>
  <div class="env-block"></div>
  <div class="env-contact"><span>www.ardoiselumen.com |</span><span>info@ardoiselumen.com</span></div>
</section>
<div class="label" style="left:443px;top:596px;width:338px">ENVELOPE ( BACK )</div>
<section class="piece env-back">
  <svg class="env-flap" width="338" height="62" viewBox="0 0 338 62"><path d="M0 0H338L322 52Q319 60 310 60H28Q19 60 16 52Z" fill="var(--navy)"/></svg>
  <div class="brand"><span class="mark"></span>ARDOISE LUMEN</div>
</section>

<!-- folder -->
<div class="label" style="left:412px;top:793px;width:365px">FOLDER DESIGN</div>
<section class="piece folder">
  <div class="folder-back">
    <div class="brand light stack"><span class="mark"></span>ARDOISE LUMEN</div>
    <div class="contact-row"><span>Address Goes Here</span><span>Phone No Goes Here</span><span>Mail Goes Here</span><span>Website Goes Here</span></div>
  </div>
  <div class="folder-front">
    <div class="brand stack"><span class="mark"></span>ARDOISE LUMEN</div>
    <div class="folder-title">TITLE HERE</div>
    <div class="web-pill"><svg viewBox="0 0 10 10"><circle cx="5" cy="5" r="4"/><path d="M1 5h8M5 1v8"/></svg>www.ardoiselumen.com</div>
  </div>
</section>

</body>
</html>
```